PTA Meeting Poster

We are looking to create a poster to invite parents of our school to our monthly PTA Meeting.

The copy should include:

PTA Meeting
This Wednesday
8:40am
in the Multi Purpose Room

All Welcome!

```html
<!DOCTYPE html>
<html lang="en">
<head>
<meta charset="utf-8">
<title>PTA Meeting Poster</title>
<link rel="stylesheet" href="https://fonts.googleapis.com/css2?family=Alex+Brush&family=Antonio:wght@200&family=Arvo:ital,wght@0,700;1,700&display=swap">
<style>
  :root {
    --page: #ffffff;
    --board-edge: #000000;
    --board-glow: #2c2c2c;
    --ink: #ffffff;
    --script: #5a5a5a;
    --badge: #4b4b4b;
  }
  html, body {
    margin: 0;
    padding: 0;
    width: 1200px;
    height: 1000px;
    overflow: hidden;
    background: var(--page);
  }
  .poster {
    display: block;
    width: 1200px;
    height: 1000px;
  }
  .headline { font-family: "Arvo", Georgia, serif; font-weight: 700; fill: var(--ink); }
  .day { font-family: "Alex Brush", cursive; fill: var(--script); }
  .detail { font-family: "Antonio", "Arial Narrow", sans-serif; font-weight: 200; fill: var(--ink); }
  .welcome { font-family: "Arvo", Georgia, serif; font-weight: 700; font-style: italic; fill: var(--ink); }
  .bracket { fill: none; stroke: var(--ink); stroke-width: 9; stroke-linejoin: round; }
  .badge { fill: var(--badge); }
</style>
</head>
<body>
<svg class="poster" viewBox="0 0 1200 1000" xmlns="http://www.w3.org/2000/svg">
  <defs>
    <radialGradient id="board-fill" cx="600" cy="480" r="520" gradientUnits="userSpaceOnUse">
      <stop offset="0" stop-color="var(--board-glow)"/>
      <stop offset="1" stop-color="var(--board-edge)"/>
    </radialGradient>
    <polygon id="burst-point" points="116,-16 135,0 116,16"/>
  </defs>

  <rect class="board" x="268" y="22" width="664" height="955" fill="url(#board-fill)"/>

  <!-- curly brackets around the headline -->
  <path class="bracket" d="M328 54 Q318 60 318 92 L318 186 Q318 206 306 213 Q318 220 318 240 L318 350 Q318 378 328 384"/>
  <path class="bracket" d="M872 54 Q882 60 882 92 L882 186 Q882 206 894 213 Q882 220 882 240 L882 350 Q882 378 872 384"/>

  <text class="headline" x="355" y="273" font-size="232" textLength="480" lengthAdjust="spacingAndGlyphs">PTA</text>
  <text class="headline" x="368" y="368" font-size="104" textLength="467" lengthAdjust="spacingAndGlyphs">MEETING</text>

  <text class="day" x="400" y="492" font-size="92" textLength="400" lengthAdjust="spacingAndGlyphs" transform="rotate(-8 400 492)">This Wednesday</text>
  <text class="detail" x="715" y="540" font-size="108" textLength="140" lengthAdjust="spacingAndGlyphs">8:40am</text>
  <text class="detail" x="372" y="648" font-size="104" textLength="486" lengthAdjust="spacingAndGlyphs">In The Multi Purpose Room</text>

  <g class="badge">
    <g transform="translate(598 802)">
      <circle r="118"/>
      <use href="#burst-point" transform="rotate(0)"/>
      <use href="#burst-point" transform="rotate(15)"/>
      <use href="#burst-point" transform="rotate(30)"/>
      <use href="#burst-point" transform="rotate(45)"/>
      <use href="#burst-point" transform="rotate(60)"/>
      <use href="#burst-point" transform="rotate(75)"/>
      <use href="#burst-point" transform="rotate(90)"/>
      <use href="#burst-point" transform="rotate(105)"/>
      <use href="#burst-point" transform="rotate(120)"/>
      <use href="#burst-point" transform="rotate(135)"/>
      <use href="#burst-point" transform="rotate(150)"/>
      <use href="#burst-point" transform="rotate(165)"/>
      <use href="#burst-point" transform="rotate(180)"/>
      <use href="#burst-point" transform="rotate(195)"/>
      <use href="#burst-point" transform="rotate(210)"/>
      <use href="#burst-point" transform="rotate(225)"/>
      <use href="#burst-point" transform="rotate(240)"/>
      <use href="#burst-point" transform="rotate(255)"/>
      <use href="#burst-point" transform="rotate(270)"/>
      <use href="#burst-point" transform="rotate(285)"/>
      <use href="#burst-point" transform="rotate(300)"/>
      <use href="#burst-point" transform="rotate(315)"/>
      <use href="#burst-point" transform="rotate(330)"/>
      <use href="#burst-point" transform="rotate(345)"/>
    </g>
    <polygon points="353,790 860,705 848,815 340,905"/>
  </g>

  <text class="welcome" x="600" y="826" font-size="74" text-anchor="middle" textLength="462" lengthAdjust="spacingAndGlyphs" transform="rotate(-10 600 805)">ALL WELCOME!</text>
</svg>
</body>
</html>
```